App Design for FlavorTrek

We need an app design for a new app called FlavorTrek, which is an app designed to inspire exploration through personalized recipe generation, local restaurant discoveries, and a vibrant community platform. It caters to food enthusiasts looking to explore global cuisines or find the best local dining spots, offering a premium experience with selected features available for free.

-------UPDATED-----
This app will be AI Driven and may not be heavily dependent on media (images,videos) at first, especially for the Recipe generator feature. Our goal is to still have attractive UI. The core functionalities we are looking are the following
1. Recipe Generator: Either user choose a specific cuisine(italian,spanish), or user inputs ingredients and get recipe, or get recipe for different occasions (xmas, thanksgiving ) and get a randomly get recipe to cook, plain simple. We expect the recipes to be displayed in clear and not too generic manner starting with ingredients and expected duration at top and then step by step guide. We also intend to enable premium users to have playful action button or icon to get unlimited recipes generated until they find what they like and also have save for later feature. These premium features should be disabled for free users and prompted to subscribe if they click them with nice popup
2. Restaurant Recommendation - will have selected pictures and will be based on inputs such as zip code and other filters such as cousine types. Premium users can filter by price range, get unlimited recommendation, see actual price range in the recommendation and can save for later where they can find it later. Free users cannot filter by price (disabled) and should see it hidden in the recommendation
3. Meal Planning - will include just simple and random meal plan with just one button or limited interaction for free, users need to subscribe to get features such as customized plan such as considering allergies or diet preferences. Premium users can also get a shopping checklist of ingredients for weekly meal preps and their step by step guide for each meal recipe.
2. Community Sharing: users can view posts and engage with community content
Updates

Hello Designers,

The initial price was not fair for the work. So I have increased it. There will also be $50-100 bonus for those who come up with great designs or for those who incorporate interesting stuff. Thank you! Much appreciated 🙏

Colors
0054AA
0677BA
7BADD7
CADEEF
E8F1F8
0094D4
00A9DD
6FCCEA
C7EBF8
E9F6FB
00AB8E
00BBA5
67D7C9
C6EFE9
E9F9F6
FFC000
F8CF3A
FAE287
FDF2CF
FEFAEE
F0912C
F2A743
F7CA91
FBE8D2
FDF5EE
EE7325
F08F49
F5BC92
FAE3D3
FDF4ED
A7469A
B969AE
D3A5CF
EDDBEB
F8F0F9
6B429C
8869AF
B7A5CE
E3DAEB
F3F0F8

```html
<!DOCTYPE html>
<html lang="en">
<head>
<meta charset="utf-8">
<title>FlavorTrek app screens</title>
<link href="https://fonts.googleapis.com/css2?family=Inter:wght@400;500;600;700&display=swap" rel="stylesheet">
<style>
:root{
  --canvas:#efefef;
  --screen:#ffffff;
  --ink:#111111;
  --muted:#555555;
  --orange:#ff8a00;
  --green:#1a8a6e;
  --pill:#ececec;
  --peach:#fdeee2;
  --yellow:#f8c93a;
  --yellow-soft:#fdf2cf;
  --teal:#13b59a;
  --teal-soft:#d3f4ee;
  --icon:#c9c9c9;
  --dark:#111111;
}
*{box-sizing:border-box;margin:0;padding:0}
html,body{width:1200px;height:482px;overflow:hidden}
body{background:var(--canvas);font-family:"Inter",sans-serif;color:var(--ink);position:relative}
.phone{position:absolute;top:43px;width:183px;height:396px;background:var(--screen);border-radius:14px;overflow:hidden}
.abs{position:absolute}
.status{position:absolute;top:7px;left:10px;right:10px;font-size:7px;display:flex;justify-content:space-between;align-items:center}
.title{position:absolute;top:27px;width:100%;text-align:center;font-size:9.3px;font-weight:500}
.subtitle{position:absolute;top:45px;width:100%;text-align:center;font-size:6.8px;font-weight:500;line-height:10px}
.question{position:absolute;top:74px;width:100%;text-align:center;font-size:7.8px;font-weight:500}
.hint{position:absolute;top:91px;width:100%;text-align:center;font-size:4.8px;font-weight:600}
.photo{position:absolute;border-radius:4px}
.diet-name{position:absolute;left:59px;font-size:8px;font-weight:500}
.diet-note{position:absolute;left:59px;width:90px;font-size:6px;color:#333;line-height:8px}
.radio{position:absolute;left:153px;width:10px;height:10px;border:1.2px solid #222;border-radius:50%}
.cta{position:absolute;left:32px;top:297px;width:119px;height:26px;background:var(--orange);border-radius:4px;color:#fff;font-size:8px;font-weight:600;display:flex;align-items:center;justify-content:center;gap:18px}
.tile-label{position:absolute;width:60px;text-align:center;font-size:6px;line-height:8px}
.lang{position:absolute;width:66px;height:20px;border-radius:10px;background:var(--pill);font-size:8px;display:flex;align-items:center;justify-content:center}
.nav{position:absolute;left:0;bottom:0;width:100%;height:50px;background:#fff;border-top:1px solid #f2f2f2}
.fab{position:absolute;left:80px;top:338px;width:24px;height:24px;border-radius:50%;background:var(--green);color:#fff;font-size:16px;line-height:22px;text-align:center;font-weight:400}
.nav svg{position:absolute;top:14px}
.home-bar{position:absolute;left:54px;top:390px;width:66px;height:2px;border-radius:1px;background:#111}
.banner{position:absolute;top:45px;left:0;width:100%;height:77px;background:var(--peach)}
.btn-dark{position:absolute;background:var(--dark);color:#fff;border-radius:3px;font-size:4.8px;font-weight:600;display:flex;align-items:center;justify-content:center}
.plan{position:absolute;width:84px;border-radius:3px;overflow:hidden}
.plan-head{height:25px;font-size:6.8px;font-weight:500;padding:10px 0 0 8px}
.meal-row{position:absolute;left:6px;width:73px;height:10px;background:#fff;border-radius:2px;font-size:4.6px;padding-left:5px;line-height:10px}
.meal-row svg{position:absolute;right:4px;top:2px}
.prep{position:absolute;left:10px;font-size:4.6px;color:#333}
.plan-text{position:absolute;width:84px;text-align:center;font-size:5.6px;line-height:10px;color:#333}
.bubble{position:absolute;background:#f4f4f4;border-radius:4px;font-size:4.4px;line-height:6.3px;padding:4px}
.rest{position:absolute;left:15px;width:154px;height:73px;border-radius:3px;overflow:hidden}
.rest-name{position:absolute;left:5px;color:#fff;font-size:6.6px;font-weight:600;line-height:10px}
.rest-by{position:absolute;left:5px;color:#ddd;font-size:3.6px}
.rating{position:absolute;right:7px;top:6px;background:#fbe8d2;border-radius:4px;font-size:3.6px;padding:1px 3px;color:#7a5200}
.rest-time{position:absolute;right:18px;color:#fff;font-size:5.2px}
.save{position:absolute;right:5px;width:10px;height:10px;border-radius:50%;background:#fff}
</style>
</head>
<body>

<!-- Shared snippets repeated per screen -->

<!-- Screen 1: diet question -->
<section class="phone" style="left:29px">
  <div class="status"><span>19:27</span><svg width="32" height="6" viewBox="0 0 32 6"><rect x="0" y="4" width="1.5" height="2" fill="#222"/><rect x="2.5" y="3" width="1.5" height="3" fill="#222"/><rect x="5" y="2" width="1.5" height="4" fill="#222"/><rect x="7.5" y="0" width="1.5" height="6" fill="#222"/><path d="M11 2.2a5 5 0 0 1 7 0M12.5 3.8a3 3 0 0 1 4 0" stroke="#222" stroke-width="1" fill="none"/><circle cx="14.5" cy="5.2" r=".8" fill="#222"/><rect x="21" y="1" width="9" height="4.5" rx="1" fill="#222"/></svg></div>
  <h1 class="title">Meal Planner</h1>
  <p class="subtitle">Help us understand your<br>diet preferences?</p>
  <p class="question">Quick question: 1/3</p>

  <div class="photo" role="img" aria-label="Bowl of leafy vegan greens" style="left:9px;top:96px;width:38px;height:39px;background:linear-gradient(135deg,#2b3a2a,#7aa25a)"></div>
  <div class="diet-name" style="top:103px">I am a Vegan</div>
  <div class="diet-note" style="top:117px">(Hide Meat, Egg and Dairy recipes)</div>
  <div class="radio" style="top:110px"></div>

  <div class="photo" role="img" aria-label="Plate of vegetarian pumpkin dish" style="left:9px;top:146px;width:38px;height:39px;background:linear-gradient(135deg,#d9dcd6,#e0902e)"></div>
  <div class="diet-name" style="top:153px">I am a Vegetarian</div>
  <div class="diet-note" style="top:168px;width:100px">(Hide Meat and Egg recipes)</div>
  <div class="radio" style="top:160px"></div>

  <div class="photo" role="img" aria-label="Baked eggs in a pan" style="left:9px;top:195px;width:38px;height:39px;background:linear-gradient(135deg,#5a3a22,#e6a24a)"></div>
  <div class="diet-name" style="top:203px">I am a Eggitarian</div>
  <div class="diet-note" style="top:218px">(Hide Meat recipes)</div>
  <div class="radio" style="top:210px"></div>

  <div class="photo" role="img" aria-label="Grilled salmon fillets" style="left:9px;top:244px;width:38px;height:39px;background:linear-gradient(135deg,#1e2a3a,#c76a4a)"></div>
  <div class="diet-name" style="top:252px">I am a Pescatarian</div>
  <div class="diet-note" style="top:267px;width:100px">(I eat fish, hide Meat recipes)</div>
  <div class="radio" style="top:259px"></div>

  <div class="cta">Next <span>&#8594;</span></div>
  <div class="nav">
    <svg style="left:20px" width="12" height="12" viewBox="0 0 12 12"><path d="M2 5.5 6 2l4 3.5V10H2z" fill="none" stroke="var(--icon)" stroke-width="1"/></svg>
    <svg style="left:52px" width="12" height="12" viewBox="0 0 12 12"><path d="M3 2h6v8.5L6 8.5 3 10.5z" fill="none" stroke="var(--green)" stroke-width="1.1"/></svg>
    <svg style="left:123px" width="12" height="12" viewBox="0 0 12 12"><path d="M3 8.5V5.5a3 3 0 0 1 6 0v3l1 1H2zM5 10.5h2" fill="none" stroke="var(--icon)" stroke-width="1"/></svg>
    <svg style="left:155px" width="12" height="12" viewBox="0 0 12 12"><circle cx="6" cy="4" r="2" fill="none" stroke="var(--icon)"/><path d="M2.5 11a3.5 3 0 0 1 7 0" fill="none" stroke="var(--icon)"/></svg>
  </div>
  <div class="fab">+</div>
  <div class="home-bar"></div>
</section>

<!-- Screen 2: interests -->
<section class="phone" style="left:221px">
  <div class="status"><span>19:27</span><svg width="32" height="6" viewBox="0 0 32 6"><rect x="0" y="4" width="1.5" height="2" fill="#222"/><rect x="2.5" y="3" width="1.5" height="3" fill="#222"/><rect x="5" y="2" width="1.5" height="4" fill="#222"/><rect x="7.5" y="0" width="1.5" height="6" fill="#222"/><path d="M11 2.2a5 5 0 0 1 7 0M12.5 3.8a3 3 0 0 1 4 0" stroke="#222" stroke-width="1" fill="none"/><circle cx="14.5" cy="5.2" r=".8" fill="#222"/><rect x="21" y="1" width="9" height="4.5" rx="1" fill="#222"/></svg></div>
  <h1 class="title">Meal Planner</h1>
  <p class="subtitle">Help us understand your<br>diet preferences?</p>
  <p class="question">Quick question: 2/3</p>
  <p class="hint">We will use this to customize your experience</p>

  <div class="photo" role="img" aria-label="Fruit loaf cake" style="left:9px;top:117px;width:47px;height:47px;background:linear-gradient(135deg,#3b2a1c,#b07a3c)"></div>
  <div class="photo" role="img" aria-label="Regional Indian idli on banana leaf" style="left:68px;top:117px;width:47px;height:47px;background:linear-gradient(135deg,#0e6a2a,#dfe8d8)"></div>
  <div class="photo" role="img" aria-label="Bowl of pumpkin soup" style="left:127px;top:117px;width:48px;height:47px;background:linear-gradient(135deg,#1c2a38,#e0701e)"></div>
  <div class="tile-label" style="left:3px;top:175px">Baking &amp; Cookies</div>
  <div class="tile-label" style="left:62px;top:175px">Regional<br>Indian recipes</div>
  <div class="tile-label" style="left:121px;top:175px">Eating healthy</div>

  <div class="photo" role="img" aria-label="Hand holding a festive dumpling" style="left:9px;top:209px;width:47px;height:47px;background:linear-gradient(135deg,#8a4a3a,#efe6dc)"></div>
  <div class="photo" role="img" aria-label="Green smoothie with kiwi" style="left:68px;top:209px;width:47px;height:47px;background:linear-gradient(135deg,#c9d6b0,#3f8a2a)"></div>
  <div class="photo" role="img" aria-label="Curry with rice" style="left:127px;top:209px;width:48px;height:47px;background:linear-gradient(135deg,#9a3a1c,#e8e8e2)"></div>
  <div class="tile-label" style="left:3px;top:267px">Fasting / Festival<br>specials</div>
  <div class="tile-label" style="left:62px;top:267px">Special diets</div>
  <div class="tile-label" style="left:121px;top:267px">Quick &amp; easy<br>cooking</div>

  <div class="cta">Next <span>&#8594;</span></div>
  <div class="nav">
    <svg style="left:20px" width="12" height="12" viewBox="0 0 12 12"><path d="M2 5.5 6 2l4 3.5V10H2z" fill="none" stroke="var(--icon)" stroke-width="1"/></svg>
    <svg style="left:52px" width="12" height="12" viewBox="0 0 12 12"><path d="M3 2h6v8.5L6 8.5 3 10.5z" fill="none" stroke="var(--green)" stroke-width="1.1"/></svg>
    <svg style="left:123px" width="12" height="12" viewBox="0 0 12 12"><path d="M3 8.5V5.5a3 3 0 0 1 6 0v3l1 1H2zM5 10.5h2" fill="none" stroke="var(--icon)" stroke-width="1"/></svg>
    <svg style="left:155px" width="12" height="12" viewBox="0 0 12 12"><circle cx="6" cy="4" r="2" fill="none" stroke="var(--icon)"/><path d="M2.5 11a3.5 3 0 0 1 7 0" fill="none" stroke="var(--icon)"/></svg>
  </div>
  <div class="fab">+</div>
  <div class="home-bar"></div>
</section>

<!-- Screen 3: language -->
<section class="phone" style="left:413px">
  <div class="status"><span>19:27</span><svg width="32" height="6" viewBox="0 0 32 6"><rect x="0" y="4" width="1.5" height="2" fill="#222"/><rect x="2.5" y="3" width="1.5" height="3" fill="#222"/><rect x="5" y="2" width="1.5" height="4" fill="#222"/><rect x="7.5" y="0" width="1.5" height="6" fill="#222"/><path d="M11 2.2a5 5 0 0 1 7 0M12.5 3.8a3 3 0 0 1 4 0" stroke="#222" stroke-width="1" fill="none"/><circle cx="14.5" cy="5.2" r=".8" fill="#222"/><rect x="21" y="1" width="9" height="4.5" rx="1" fill="#222"/></svg></div>
  <h1 class="title">Meal Planner</h1>
  <p class="subtitle">Help us understand your<br>diet preferences?</p>
  <p class="question">Quick question: 3/3</p>
  <p class="hint">Select your desired language preference</p>

  <div class="lang" style="left:17px;top:118px">English</div><div class="lang" style="left:99px;top:118px">Hindi</div>
  <div class="lang" style="left:17px;top:146px">Marathi</div><div class="lang" style="left:99px;top:146px">Gujarati</div>
  <div class="lang" style="left:17px;top:175px">Tamil</div><div class="lang" style="left:99px;top:175px">Telugu</div>
  <div class="lang" style="left:17px;top:203px">Kannada</div><div class="lang" style="left:99px;top:203px">Malayalam</div>
  <div class="lang" style="left:17px;top:231px">Bengali</div><div class="lang" style="left:99px;top:231px">Oriya</div>
  <div class="lang" style="left:17px;top:259px">Punjabi</div><div class="lang" style="left:99px;top:259px">Assamese</div>

  <div class="cta" style="left:35px">Finish <span>&#8594;</span></div>
  <div class="nav">
    <svg style="left:20px" width="12" height="12" viewBox="0 0 12 12"><path d="M2 5.5 6 2l4 3.5V10H2z" fill="none" stroke="var(--icon)" stroke-width="1"/></svg>
    <svg style="left:52px" width="12" height="12" viewBox="0 0 12 12"><path d="M3 2h6v8.5L6 8.5 3 10.5z" fill="none" stroke="var(--green)" stroke-width="1.1"/></svg>
    <svg style="left:123px" width="12" height="12" viewBox="0 0 12 12"><path d="M3 8.5V5.5a3 3 0 0 1 6 0v3l1 1H2zM5 10.5h2" fill="none" stroke="var(--icon)" stroke-width="1"/></svg>
    <svg style="left:155px" width="12" height="12" viewBox="0 0 12 12"><circle cx="6" cy="4" r="2" fill="none" stroke="var(--icon)"/><path d="M2.5 11a3.5 3 0 0 1 7 0" fill="none" stroke="var(--icon)"/></svg>
  </div>
  <div class="fab">+</div>
  <div class="home-bar"></div>
</section>

<!-- Screen 4: manage meals -->
<section class="phone" style="left:605px">
  <div class="status"><span>19:27</span><svg width="32" height="6" viewBox="0 0 32 6"><rect x="0" y="4" width="1.5" height="2" fill="#222"/><rect x="2.5" y="3" width="1.5" height="3" fill="#222"/><rect x="5" y="2" width="1.5" height="4" fill="#222"/><rect x="7.5" y="0" width="1.5" height="6" fill="#222"/><path d="M11 2.2a5 5 0 0 1 7 0M12.5 3.8a3 3 0 0 1 4 0" stroke="#222" stroke-width="1" fill="none"/><circle cx="14.5" cy="5.2" r=".8" fill="#222"/><rect x="21" y="1" width="9" height="4.5" rx="1" fill="#222"/></svg></div>
  <h1 class="title">Manage your meals</h1>
  <div class="banner">
    <div class="abs" style="left:14px;top:20px;font-size:6.6px">Need help in planning?</div>
    <div class="abs" style="left:14px;top:29px;font-size:9px;font-weight:700">Ai-Generated meals!</div>
    <div class="abs" style="left:14px;top:41px;font-size:4.6px;color:#444">based on your preferences</div>
    <div class="btn-dark" style="left:14px;top:50px;width:64px;height:15px;font-size:5.4px">Auto-Generate &gt;&gt;</div>
    <div class="abs" role="img" aria-label="Illustrated Indian thali with bowls of curries" style="left:108px;top:5px;width:72px;height:68px;border-radius:50%;background:radial-gradient(circle,#f5e6c8 0%,#e8a45a 45%,#c9d9e6 70%,rgba(253,238,226,0) 72%)"></div>
  </div>

  <div class="plan" style="left:7px;top:127px;height:118px;background:var(--yellow-soft)">
    <div class="plan-head" style="background:var(--yellow)">TOMORROW'S PLAN</div>
    <div class="meal-row" style="top:39px">Breakfast<svg width="6" height="6" viewBox="0 0 6 6"><path d="M1 5h1l3-3-1-1-3 3z" fill="none" stroke="#333" stroke-width=".6"/></svg></div>
    <div class="meal-row" style="top:53px">Lunch<svg width="6" height="6" viewBox="0 0 6 6"><path d="M1 5h1l3-3-1-1-3 3z" fill="none" stroke="#333" stroke-width=".6"/></svg></div>
    <div class="meal-row" style="top:67px">Dinner<svg width="6" height="6" viewBox="0 0 6 6"><path d="M1 5h1l3-3-1-1-3 3z" fill="none" stroke="#333" stroke-width=".6"/></svg></div>
    <div class="prep" style="top:80px">&#128276;&#xFE0E; Prep required</div>
    <div class="btn-dark" style="left:8px;top:92px;width:70px;height:15px">Share in Community</div>
  </div>
  <div class="plan" style="left:93px;top:127px;height:118px;background:var(--teal-soft)">
    <div class="plan-head" style="background:var(--teal);color:#fff">ONCOMING'S PLAN</div>
    <div class="meal-row" style="top:39px">Breakfast<svg width="6" height="6" viewBox="0 0 6 6"><path d="M1 5h1l3-3-1-1-3 3z" fill="none" stroke="#333" stroke-width=".6"/></svg></div>
    <div class="meal-row" style="top:53px">Lunch<svg width="6" height="6" viewBox="0 0 6 6"><path d="M1 5h1l3-3-1-1-3 3z" fill="none" stroke="#333" stroke-width=".6"/></svg></div>
    <div class="meal-row" style="top:67px">Dinner<svg width="6" height="6" viewBox="0 0 6 6"><path d="M1 5h1l3-3-1-1-3 3z" fill="none" stroke="#333" stroke-width=".6"/></svg></div>
    <div class="prep" style="top:80px">&#128276;&#xFE0E; Prep required</div>
    <div class="btn-dark" style="left:8px;top:92px;width:70px;height:15px">Share in Community</div>
  </div>

  <div class="plan" style="left:7px;top:252px;height:100px;background:var(--yellow-soft)">
    <div class="plan-head" style="background:var(--yellow)">PLAN YOUR MEALS</div>
    <svg class="abs" style="left:35px;top:30px" width="15" height="15" viewBox="0 0 15 15"><rect x="1" y="2.5" width="13" height="11" rx="1" fill="none" stroke="#222" stroke-width="1.1"/><path d="M1 6h13M4.5 1v3M10.5 1v3" stroke="#222" stroke-width="1.1"/><rect x="3.5" y="8.5" width="2" height="2" fill="#222"/><rect x="6.5" y="8.5" width="2" height="2" fill="#222"/></svg>
    <div class="plan-text" style="top:53px">Select a date &amp; start<br>adding the recipes!</div>
    <div class="btn-dark" style="left:8px;top:70px;width:70px;height:16px">Go to Meal Planner</div>
  </div>
  <div class="plan" style="left:93px;top:252px;height:100px;background:var(--teal-soft)">
    <div class="plan-head" style="background:var(--teal);color:#fff">TRACK PROGRESS</div>
    <svg class="abs" style="left:34px;top:32px" width="16" height="16" viewBox="0 0 16 16"><circle cx="8" cy="8" r="6.5" fill="none" stroke="#222" stroke-width="1.2"/><circle cx="8" cy="8" r="3.8" fill="none" stroke="#222" stroke-width="1"/><path d="M8 8l3.5-3.5" stroke="#222" stroke-width="1.2"/></svg>
    <div class="plan-text" style="top:53px">Get smart insights with Ai<br>powered tracker!</div>
    <div class="btn-dark" style="left:8px;top:70px;width:70px;height:16px">Go to Meal Planner</div>
  </div>

  <div class="nav">
    <svg style="left:20px" width="12" height="12" viewBox="0 0 12 12"><path d="M2 5.5 6 2l4 3.5V10H2z" fill="none" stroke="var(--icon)" stroke-width="1"/></svg>
    <svg style="left:52px" width="12" height="12" viewBox="0 0 12 12"><path d="M3 2h6v8.5L6 8.5 3 10.5z" fill="none" stroke="var(--green)" stroke-width="1.1"/></svg>
    <svg style="left:123px" width="12" height="12" viewBox="0 0 12 12"><path d="M3 8.5V5.5a3 3 0 0 1 6 0v3l1 1H2zM5 10.5h2" fill="none" stroke="var(--icon)" stroke-width="1"/></svg>
    <svg style="left:155px" width="12" height="12" viewBox="0 0 12 12"><circle cx="6" cy="4" r="2" fill="none" stroke="var(--icon)"/><path d="M2.5 11a3.5 3 0 0 1 7 0" fill="none" stroke="var(--icon)"/></svg>
  </div>
  <div class="fab">+</div>
  <div class="home-bar"></div>
</section>

<!-- Screen 5: AI chat -->
<section class="phone" style="left:797px">
  <div class="status"><span>19:27</span><svg width="32" height="6" viewBox="0 0 32 6"><rect x="0" y="4" width="1.5" height="2" fill="#222"/><rect x="2.5" y="3" width="1.5" height="3" fill="#222"/><rect x="5" y="2" width="1.5" height="4" fill="#222"/><rect x="7.5" y="0" width="1.5" height="6" fill="#222"/><path d="M11 2.2a5 5 0 0 1 7 0M12.5 3.8a3 3 0 0 1 4 0" stroke="#222" stroke-width="1" fill="none"/><circle cx="14.5" cy="5.2" r=".8" fill="#222"/><rect x="21" y="1" width="9" height="4.5" rx="1" fill="#222"/></svg></div>
  <svg class="abs" style="left:16px;top:29px" width="9" height="7" viewBox="0 0 9 7"><path d="M8.5 3.5H1M4 .5l-3 3 3 3" fill="none" stroke="#111" stroke-width="1"/></svg>
  <div class="abs" style="left:63px;top:27px;display:flex;align-items:center;gap:3px;font-size:7px;font-weight:500"><span style="width:9px;height:9px;border:1px solid #222;border-radius:50%;display:inline-block"></span>FlavorTrek Ai</div>
  <div class="abs" style="left:158px;top:25px;font-size:8px;font-weight:700;letter-spacing:.5px">···</div>

  <div class="abs" style="left:121px;top:56px;font-size:7px;font-weight:500">Alex Rowe</div>
  <div class="abs" role="img" aria-label="User profile photo" style="left:156px;top:53px;width:15px;height:15px;border-radius:50%;background:linear-gradient(135deg,#d9d2c8,#8a7a6a)"></div>
  <div class="bubble" style="left:39px;top:69px;width:112px">i want to know the species of strawberry used in this charcuterie board?</div>

  <div class="abs" style="left:11px;top:97px;width:15px;height:15px;border-radius:50%;background:var(--dark)"></div>
  <div class="abs" style="left:30px;top:99px;font-size:7px;font-weight:500">FlavorTrek Ai</div>
  <div class="bubble" style="left:29px;top:111px;width:124px;height:226px;padding:5px 5px">
    Strawberry varieties: list of popular varieties<br><br>
    The variety of strawberry types is huge. We give you an overview of popular strawberry varieties and types. There are early to late varieties that you can combine for a rich and long harvest. A distinction is also made between ever bearing and single-bearing varieties. You can find out what these are and what examples of varieties there are here.<br><br>
    How many strawberry varieties are there?<br><br>
    It was only with the discovery of America that new species with larger fruits spread to our latitudes. Countless new varieties were created and we now have over 1000 different varieties worldwide. There are variety-specific preferences of the plants for the location and climate, as well as differences in taste, appearance and growth. In addition, old varieties are often not self-fertile. Self-fertile varieties that do not depend on pollinators to produce fruit were only created through breeding. In Central Europe, there are around 20 varieties that are grown for sale as strawberries. You can find out how to grow strawberries with tips on planting, sowing and picking here....
  </div>

  <div class="abs" style="left:12px;top:346px;width:129px;height:25px;border:1px solid #e2e2e2;border-radius:3px;display:flex;align-items:center;padding-left:8px;gap:4px;font-size:7px;color:#777">
    <svg width="8" height="8" viewBox="0 0 8 8"><circle cx="4" cy="4" r="3.3" fill="none" stroke="#777" stroke-width=".7"/><path d="M2.6 4.8a1.6 1.6 0 0 0 2.8 0" fill="none" stroke="#777" stroke-width=".6"/></svg>Type something...
  </div>
  <div class="abs" style="left:146px;top:346px;width:25px;height:25px;border-radius:3px;background:var(--orange)"><svg style="position:absolute;left:7px;top:7px" width="11" height="11" viewBox="0 0 11 11"><path d="M1 1l9 4.5L1 10l1.5-4.5z" fill="#fff"/></svg></div>
  <div class="home-bar"></div>
</section>

<!-- Screen 6: restaurants -->
<section class="phone" style="left:989px">
  <div class="status"><span>19:27</span><svg width="32" height="6" viewBox="0 0 32 6"><rect x="0" y="4" width="1.5" height="2" fill="#222"/><rect x="2.5" y="3" width="1.5" height="3" fill="#222"/><rect x="5" y="2" width="1.5" height="4" fill="#222"/><rect x="7.5" y="0" width="1.5" height="6" fill="#222"/><path d="M11 2.2a5 5 0 0 1 7 0M12.5 3.8a3 3 0 0 1 4 0" stroke="#222" stroke-width="1" fill="none"/><circle cx="14.5" cy="5.2" r=".8" fill="#222"/><rect x="21" y="1" width="9" height="4.5" rx="1" fill="#222"/></svg></div>
  <h1 class="title">Restaurant Recommendation</h1>

  <div class="rest" role="img" aria-label="Warm wooden restaurant interior" style="top:49px;background:linear-gradient(135deg,#3a2412,#a8692e 60%,#4a2c14)">
    <div class="rating">&#9733; 4.0</div>
    <div class="rest-name" style="top:44px">Restaurant<br>Recommendation</div>
    <div class="rest-by" style="top:64px">By Chef Omar</div>
    <div class="rest-time" style="top:61px">20 min</div><div class="save" style="top:59px"></div>
  </div>
  <div class="rest" role="img" aria-label="Dining room with red chairs" style="top:132px;background:linear-gradient(135deg,#5a4a2a,#b0451e 55%,#e0c8a0)">
    <div class="rating">&#9733; 4.0</div>
    <div class="rest-name" style="top:44px">Restaurant<br>Recommendation</div>
    <div class="rest-by" style="top:64px">By Lena Park</div>
    <div class="rest-time" style="top:61px">20 min</div><div class="save" style="top:59px"></div>
  </div>
  <div class="rest" role="img" aria-label="Dim restaurant with red lighting" style="top:215px;background:linear-gradient(135deg,#2a1410,#7a3218 55%,#3a1a10)">
    <div class="rating">&#9733; 4.0</div>
    <div class="rest-name" style="top:44px">Restaurant<br>Recommendation</div>
    <div class="rest-by" style="top:64px">By Tara Vance</div>
    <div class="rest-time" style="top:61px">&#9201;&#xFE0E; 20 min</div><div class="save" style="top:59px"></div>
  </div>
  <div class="rest" role="img" aria-label="Green plant-filled cafe interior" style="top:298px;background:linear-gradient(135deg,#2a3a2a,#5a7a4a 55%,#1e2a22)">
    <div class="rating">&#9733; 3.0</div>
  </div>

  <div class="nav">
    <svg style="left:20px" width="12" height="12" viewBox="0 0 12 12"><path d="M2 5.5 6 2l4 3.5V10H2z" fill="none" stroke="var(--icon)" stroke-width="1"/></svg>
    <svg style="left:52px" width="12" height="12" viewBox="0 0 12 12"><path d="M3 2h6v8.5L6 8.5 3 10.5z" fill="none" stroke="var(--green)" stroke-width="1.1"/></svg>
    <svg style="left:123px" width="12" height="12" viewBox="0 0 12 12"><path d="M3 8.5V5.5a3 3 0 0 1 6 0v3l1 1H2zM5 10.5h2" fill="none" stroke="var(--icon)" stroke-width="1"/></svg>
    <svg style="left:155px" width="12" height="12" viewBox="0 0 12 12"><circle cx="6" cy="4" r="2" fill="none" stroke="var(--icon)"/><path d="M2.5 11a3.5 3 0 0 1 7 0" fill="none" stroke="var(--icon)"/></svg>
  </div>
  <div class="fab">+</div>
  <div class="home-bar"></div>
</section>

</body>
</html>
```